Retail Business Needs a New Ecommerce Store Design

We need a new web design for a company called Bell Forge and Canopy (see attached logos). We sell a range of Shade Cloth and horticultural products. We want the layout to be similar to this website http://www.wombleparkcamp.com.au/
and we like the design of the shopping cart and checkout. But we don't like the text used on this site and the glare.
We also like the layout of this site http://www.dorvantel.com/
We really like the look and feel of this website http://www.moxbelford.com.au/
We want a bright website. You can use any colours that work with our logo besides blue. Fonts are to be striking and visible to the older generation, and the website is to be very user friendly and easy to navigate. I have attached a word doc of all the features we would like include. Don't pay any attention to the colours I have used and in regards to layout take this as a rough guide only. We want all our major categories to be easily seen on every page. The website will be built in drupal.
Key Features of the Site:
- Message box on side of page
- Special Search Box where you can search by application and Fabric type similar to the search box found here: http://www.moxbelford.com.au/product-search
- An area on the product page that shows what else customers bought
We need the design submitted as a psd.
Pages needed for the Site:
Home
Product Page
Product Category Page
Shopping Cart Page
Checkout Page
If you have any questions in regards to this project don't hesitate to ask.
Updates
Hey all,
Thanks for your submissions we will get back to you with some feedback in the next few days after we have a meeting.
Target Market(s)
Our main target market is mostly Males over 30.
Industry/Entity Type
Business
Number of Pages Required
5+ page
Look and feel
Each slider illustrates characteristics of the customer's brand and the style your logo design should communicate.

```html
<!DOCTYPE html>
<html lang="en">
<head>
<meta charset="utf-8">
<title>Bell Forge and Canopy</title>
<link href="https://fonts.googleapis.com/css2?family=Arimo:wght@400;700&family=Open+Sans:wght@400;600;700&display=swap" rel="stylesheet">
<style>
:root{
  --green:#0c6a37;
  --green-dark:#08552b;
  --text-grey:#8c8c8c;
  --line:#dcdcdc;
  --footer:#333333;
  --footer-text:#d6d6d6;
  --white:#ffffff;
}
*{box-sizing:border-box;margin:0;padding:0}
html,body{width:1086px;height:1200px;overflow:hidden;background:var(--white);font-family:"Arimo",Arial,sans-serif}
.page{position:relative;width:1086px;height:1200px}
.top-rule{position:absolute;left:0;top:0;width:1086px;height:3px;background:var(--green)}
.brand{position:absolute;left:118px;top:22px;display:flex;align-items:center;gap:12px}
.brand-name{font-family:"Open Sans",sans-serif;font-weight:700;font-size:26px;line-height:28px;color:var(--green);width:170px}
.brand-dot{width:52px;height:52px;border-radius:50%;background:var(--green)}
.cart{position:absolute;right:120px;top:19px;font-size:13px;color:var(--text-grey);font-family:"Open Sans",sans-serif;display:flex;align-items:center;gap:10px}
.cart b{font-weight:400;color:var(--green)}
.contact-line{position:absolute;left:444px;top:67px;font-size:12.5px;color:#555}
.contact-line span{color:var(--green)}
.search{position:absolute;left:702px;top:56px;width:264px;height:37px;display:flex}
.search-field{flex:1;border:1px solid #ccc;border-right:none;font-size:10px;color:#777;padding:12px 11px}
.search-btn{width:42px;background:var(--green);display:flex;align-items:center;justify-content:center}
.main-nav{position:absolute;left:118px;top:111px;width:848px;height:51px;background:var(--green);display:flex;justify-content:space-around;align-items:center;padding:0 8px}
.main-nav a{color:var(--white);text-decoration:none;font-size:12.5px}
.hero{position:absolute;left:120px;top:167px;width:602px;height:271px;background:linear-gradient(180deg,#5d7a55 0%,#8a8b8a 40%,#4e6e3a 75%,#6a8a3a 100%)}
.hero-arrows{position:absolute;right:18px;bottom:12px}
.finder{position:absolute;left:730px;top:167px;width:236px;height:271px;border:1px solid var(--line)}
.finder-title{height:40px;padding:13px 0 0 24px;font-family:"Open Sans",sans-serif;font-weight:700;font-size:11.5px;line-height:14px;white-space:nowrap;color:var(--green)}
.finder-row{height:38.2px;border-top:1px solid var(--line);padding:12px 23px;font-size:11.5px;line-height:14px;color:var(--text-grey);white-space:nowrap}
.finder-row.active{position:relative;height:40px;background:var(--green);color:var(--white);font-family:"Open Sans",sans-serif;font-weight:700;font-size:11.5px;border-top:none;padding:13px 24px;margin:0 -1px}
.finder-row.active::before{content:"";position:absolute;left:0;top:14px;border:6px solid transparent;border-left-color:var(--white)}
.section-title{position:absolute;left:118px;top:466px;font-family:"Open Sans",sans-serif;font-weight:400;font-size:14.5px;color:var(--green)}
.section-arrows{position:absolute;left:938px;top:469px}
.products{position:absolute;left:118px;top:501px;width:848px;display:flex;justify-content:space-between}
.product{width:204px}
.product-image{height:151px;border:1px solid var(--line)}
.product-name{height:40px;border-bottom:1px solid var(--line);text-align:center;padding-top:13px;font-size:12px;color:var(--text-grey)}
.tent{background:linear-gradient(180deg,#fff 20%,#cfc6a8 50%,#fff 85%)}
.furniture{background:linear-gradient(180deg,#fff 25%,#8a8078 55%,#fff 85%)}
.grill{background:linear-gradient(180deg,#fff 25%,#cfd2d3 55%,#fff 85%)}
.gazebo{background:linear-gradient(180deg,#fff 20%,#3d4e86 55%,#fff 85%)}
.banner{position:absolute;left:118px;top:722px;width:849px;height:370px;background:#ececec}
.banner-image{position:absolute;left:15px;top:15px;width:819px;height:341px;background:linear-gradient(180deg,#9fb4bf 0%,#c8d4d6 35%,#7f9a62 65%,#3f7a26 100%)}
.banner-caption{position:absolute;left:56px;top:288px;width:739px;height:56px;background:rgba(40,40,40,.45);color:var(--white);text-align:center;font-size:19px;line-height:22px;padding-top:17px;white-space:nowrap}
.slide-btn{position:absolute;top:160px;width:25px;height:50px;background:var(--white)}
.slide-btn.prev{left:15px;border-radius:0 25px 25px 0}
.slide-btn.next{right:15px;border-radius:25px 0 0 25px}
.slide-btn svg{position:absolute;top:17px}
.side-contact{position:absolute;left:1049px;top:430px;width:37px;height:164px;background:var(--green);border-radius:3px 0 0 3px}
.side-contact span{position:absolute;left:8px;top:112px;transform:rotate(-90deg);transform-origin:0 0;color:var(--white);font-family:"Open Sans",sans-serif;font-weight:700;font-size:15px;line-height:20px;white-space:nowrap}
.footer{position:absolute;left:0;top:1105px;width:1086px;height:95px;background:var(--footer)}
.footer-links{position:absolute;left:119px;top:26px;font-size:10.5px;color:var(--footer-text)}
.footer-links i{font-style:normal;margin:0 8px}
.copyright{position:absolute;left:119px;top:59px;font-size:10.5px;color:var(--footer-text)}
.social{position:absolute;left:836px;top:37px;display:flex;gap:7px}
.social div{width:28px;height:27px;border:1px solid #666}
</style>
</head>
<body>
<div class="page">
  <div class="top-rule"></div>

  <div class="brand">
    <div class="brand-name">Bell Forge and Canopy</div>
    <div class="brand-dot"></div>
  </div>

  <div class="cart">
    <svg width="16" height="18" viewBox="0 0 16 18"><rect x="1" y="5" width="14" height="12" fill="none" stroke="#777" stroke-width="1.4"/><path d="M5 7V3a3 3 0 0 1 6 0v4" fill="none" stroke="#777" stroke-width="1.4"/></svg>
    <div>CART 0 items for <b>$0.00</b></div>
  </div>

  <div class="contact-line"><span>Contact Us</span> : sales@bellforgecanopy.com.au</div>

  <div class="search">
    <div class="search-field">Enter Any Keyword........</div>
    <div class="search-btn"><svg width="14" height="14" viewBox="0 0 14 14"><circle cx="5.5" cy="5.5" r="4" fill="none" stroke="#fff" stroke-width="2"/><path d="M8.5 8.5L13 13" stroke="#fff" stroke-width="2.4"/></svg></div>
  </div>

  <nav class="main-nav">
    <a>Shadecloth</a><a>Greenhouse Film</a><a>Specialty Nets</a><a>Weedmat</a><a>Polythene</a><a>Windbreak</a><a>Nail Guns &amp; Nails</a><a>Accessories</a>
  </nav>

  <div class="hero" role="img" aria-label="Suburban home with lit windows and a landscaped garden">
    <svg class="hero-arrows" width="34" height="22" viewBox="0 0 34 22"><path d="M11 2L3 11l8 9M23 2l8 9-8 9" fill="none" stroke="#fff" stroke-width="3"/></svg>
  </div>

  <div class="finder">
    <div class="finder-title">WHAT THEY ARE LOOKING FOR</div>
    <div class="finder-row active">PAGOLA OR BBQ AREA</div>
    <div class="finder-row">BULID&nbsp; A GREENHOUSE</div>
    <div class="finder-row">PAGOLA OR BBQ AREA</div>
    <div class="finder-row">BULID&nbsp; A GREENHOUSE</div>
    <div class="finder-row">PAGOLA OR BBQ AREA</div>
    <div class="finder-row">PAGOLA OR BBQ AREA</div>
  </div>

  <h2 class="section-title">CLEARANCE STOCK/SALES</h2>
  <svg class="section-arrows" width="28" height="10" viewBox="0 0 28 10"><path d="M6 1L2 5l4 4M22 1l4 4-4 4" fill="none" stroke="#999" stroke-width="1.2"/></svg>

  <div class="products">
    <div class="product"><div class="product-image tent" role="img" aria-label="Canvas touring tent"></div><div class="product-name">TOURING &amp; POP-UP TENTS</div></div>
    <div class="product"><div class="product-image furniture" role="img" aria-label="Wicker outdoor lounge setting"></div><div class="product-name">OUTDOOR FURNITURE</div></div>
    <div class="product"><div class="product-image grill" role="img" aria-label="Stainless steel barbecue"></div><div class="product-name">BBQ'S</div></div>
    <div class="product"><div class="product-image gazebo" role="img" aria-label="Navy gazebo with screen walls"></div><div class="product-name">GAZEBOS/SCREEN ROOMS</div></div>
  </div>

  <div class="banner">
    <div class="banner-image" role="img" aria-label="Interior of a poly tunnel greenhouse with rows of green seedlings"></div>
    <div class="slide-btn prev"><svg width="14" height="16" viewBox="0 0 14 16" style="left:5px"><path d="M9 1L3 8l6 7" fill="none" stroke="#777" stroke-width="2"/></svg></div>
    <div class="slide-btn next"><svg width="14" height="16" viewBox="0 0 14 16" style="left:8px"><path d="M4 1l6 7-6 7" fill="none" stroke="#777" stroke-width="2"/></svg></div>
    <div class="banner-caption">90% Shade Cloth 1.83m X 5m,Greenhouse Film,Shadecloth in Multiple Colours</div>
  </div>

  <div class="side-contact">
    <span>CONTACT US</span>
    <svg width="22" height="20" viewBox="0 0 22 20" style="position:absolute;left:8px;top:132px"><circle cx="10" cy="11" r="8" fill="#fff"/></svg>
  </div>

  <footer class="footer">
    <div class="footer-links">Shadecloth<i>|</i>Greenhouse Film<i>|</i>Specialty Nets<i>|</i>Weedmat<i>|</i>Polythene<i>|</i>Windbreak<i>|</i>Nail Guns &amp; Nails<i>|</i>Accessories</div>
    <div class="copyright">© Copy Rights 2014 Ecommerce Site. All Rights Reseved.</div>
    <div class="social"><div></div><div></div><div></div><div></div></div>
  </footer>
</div>
</body>
</html>
```